Maple Crest Staffing Agency

I need to make a brochure/catalogue that represent our company, telling our clients what we do, our values, fields of industry that we taken care of, so they know who we are, what we did, and how we do it.
I do have a logo and simple brochure design before that i really need to upgrade (i will give it as an example on this attachment).

What I want in the new design is :
1. More pictures and little bit of explanation in each industry we work with.
2. Attractive design that make people LOOK at the brochure and not just throw it in the trash.
3. Still use the combination color of the company logo itself, which is Golden Brown.

```html
<!DOCTYPE html>
<html lang="en">
<head>
<meta charset="utf-8">
<title>Maple Crest Staffing Agency – Tri-fold Brochure</title>
<link href="https://fonts.googleapis.com/css2?family=Montserrat:wght@400;700;800;900&family=Open+Sans:ital,wght@0,400;0,600;0,700;1,600;1,700&family=Raleway:wght@300;400;700;800&display=swap" rel="stylesheet">
<style>
  :root {
    --gold: #a8893a;
    --gold-light: #c7a84e;
    --gold-dark: #86692a;
    --black: #0c0c0c;
    --charcoal: #2a2a2a;
    --paper: #f2f2f2;
    --paper-shade: #e2e2e2;
    --ink: #2b2b2b;
    --white: #ffffff;
    --stage: #ececec;
  }
  * { box-sizing: border-box; margin: 0; padding: 0; }
  html, body { width: 720px; height: 1200px; overflow: hidden; }
  body { background: var(--stage); font-family: "Open Sans", sans-serif; color: var(--ink); position: relative; }

  .spread { position: absolute; left: 20px; width: 680px; height: 525px; overflow: hidden; box-shadow: 0 6px 18px rgba(0,0,0,.18); }
  .spread--outside { top: 30px; background: var(--black); }
  .spread--inside { top: 620px; background: var(--paper); }
  .spread__art { position: absolute; inset: 0; width: 680px; height: 525px; }

  .panel { position: absolute; top: 0; width: 227px; height: 525px; }
  .panel--1 { left: 0; } .panel--2 { left: 227px; } .panel--3 { left: 453px; }

  .heading { font-family: "Raleway", sans-serif; font-weight: 300; font-size: 15px; letter-spacing: .3px; text-transform: uppercase; line-height: 1.1; }
  .heading b { font-weight: 800; }
  .heading--gold-accent b { color: var(--gold-light); }
  .rule { height: 1px; background: currentColor; opacity: .6; margin-top: 5px; }

  .body-copy { font-size: 6.6px; line-height: 1.45; }

  /* Outside — panel 1 */
  .agent { position: absolute; left: 18px; top: 24px; width: 192px; color: var(--white); }
  .agent .body-copy { margin-top: 12px; text-align: justify; }
  .photo-frame { position: absolute; left: 18px; width: 192px; height: 100px; border: 1px solid var(--gold-light); padding: 4px; }
  .photo-frame__fill { width: 100%; height: 100%; }
  .photo-frame--casino { top: 300px; }
  .photo-frame--casino .photo-frame__fill { background: linear-gradient(135deg, #3a2a26, #7a3530 55%, #2a2220); }
  .photo-frame--warehouse { top: 412px; }
  .photo-frame--warehouse .photo-frame__fill { background: linear-gradient(120deg, #5b4a3a, #a08a5c 50%, #c8c23a 70%, #4a3e32); }

  /* Outside — panel 2 */
  .locations { position: absolute; left: 22px; top: 22px; width: 185px; color: var(--white); }
  .locations__list { display: grid; grid-template-columns: 1fr 1fr; margin-top: 9px; list-style: none; font-family: "Raleway", sans-serif; font-size: 8px; row-gap: 3px; }
  .locations__list li { display: flex; align-items: center; gap: 4px; }
  .contact { position: absolute; left: 0; top: 408px; width: 227px; text-align: center; color: var(--white); }
  .contact__pill { display: inline-block; background: var(--black); border-radius: 12px; padding: 4px 18px; font-family: "Raleway", sans-serif; font-size: 12px; font-weight: 300; }
  .contact__pill b { font-weight: 800; }
  .contact__line { font-size: 7px; margin-top: 4px; display: flex; justify-content: center; align-items: center; gap: 4px; }
  .contact__phone { font-family: "Montserrat", sans-serif; font-weight: 800; font-size: 12px; }

  /* Outside — panel 3 */
  .brand { position: absolute; left: 0; top: 36px; width: 227px; display: flex; justify-content: center; align-items: center; gap: 8px; }
  .brand__dot { width: 14px; height: 14px; background: var(--gold-light); border-radius: 50%; }
  .brand__name { font-family: "Raleway", sans-serif; font-weight: 800; font-size: 15px; color: var(--gold-light); letter-spacing: .5px; }
  .tagline { position: absolute; left: 0; top: 405px; width: 227px; text-align: center; color: var(--white); font-family: "Montserrat", sans-serif; font-weight: 900; font-size: 20px; line-height: 1.05; }
  .tagline__band { display: inline-block; background: var(--gold); color: var(--black); padding: 0 22px; margin-top: 2px; }
  .web-pill { position: absolute; left: 22px; top: 485px; width: 183px; border: 1px solid var(--gold-light); border-radius: 10px; text-align: center; font-size: 7.5px; color: var(--white); padding: 3px 0; }

  /* Inside — panel 1 */
  .about { position: absolute; left: 16px; top: 20px; width: 196px; }
  .tab { display: inline-block; font-family: "Open Sans", sans-serif; font-weight: 700; font-size: 7.5px; padding: 1px 14px 1px 6px; clip-path: polygon(0 0, 100% 0, 88% 100%, 0 100%); margin-top: 6px; }
  .tab--gold { background: var(--gold); color: var(--white); }
  .tab--black { background: var(--charcoal); color: var(--white); }
  .about .body-copy { font-size: 6px; margin-top: 2px; }
  .team-photo { position: absolute; left: 0; bottom: 0; width: 227px; height: 100px; background: linear-gradient(90deg, #c9b27a, #6e7a88 35%, #4b4b55 55%, #b04a3a 75%, #9a9fa8); }

  /* Inside — panel 2 */
  .why-staffing { position: absolute; left: 14px; top: 18px; width: 200px; color: var(--white); }
  .why-staffing .body-copy { font-size: 6px; }
  .industries { position: absolute; left: 14px; top: 296px; width: 200px; color: var(--white); }
  .industries__list { list-style: none; margin-top: 8px; font-family: "Montserrat", sans-serif; font-weight: 800; font-size: 11px; line-height: 1.7; }
  .industries__list li::before { content: "» "; }
  .consultant-photo { position: absolute; left: 368px; top: 392px; width: 110px; height: 133px; background: linear-gradient(180deg, #d9cfc0, #7f9cc4 55%, #5b7aa8); }

  /* Inside — panel 3 */
  .why-choose { position: absolute; left: 14px; top: 18px; width: 200px; }
  .why-choose .body-copy { font-size: 6px; }
  .subhead { font-style: italic; font-weight: 700; color: var(--gold); }
  .closing { font-style: italic; font-weight: 600; margin-top: 5px; }
  .slogan { position: absolute; left: 0; top: 432px; width: 227px; height: 93px; background: var(--gold); color: var(--white); text-align: center; font-family: "Montserrat", sans-serif; font-weight: 900; }
  .slogan__main { font-size: 16px; line-height: 1.05; padding-top: 12px; }
  .slogan__strip { background: var(--charcoal); font-size: 11px; margin-top: 8px; padding: 4px 0; }
</style>
</head>
<body>

<!-- OUTSIDE SPREAD -->
<section class="spread spread--outside" aria-label="Brochure outside spread">
  <svg class="spread__art" viewBox="0 0 680 525" xmlns="http://www.w3.org/2000/svg">
    <defs>
      <linearGradient id="gold-fill" x1="0" y1="0" x2="1" y2="1">
        <stop offset="0" stop-color="#b39444"/><stop offset="1" stop-color="#8a6d2c"/>
      </linearGradient>
      <linearGradient id="staff-photo" x1="0" y1="0" x2="1" y2="0">
        <stop offset="0" stop-color="#6b4a36"/><stop offset=".2" stop-color="#e9e2d8"/>
        <stop offset=".45" stop-color="#2d2a2a"/><stop offset=".6" stop-color="#f1ece6"/>
        <stop offset=".8" stop-color="#d8c7a8"/><stop offset="1" stop-color="#5a3a2a"/>
      </linearGradient>
    </defs>
    <rect x="227" y="0" width="453" height="525" fill="#0c0c0c"/>
    <g role="img" aria-label="Group photo of smiling hospitality and service staff in uniforms">
      <rect x="227" y="120" width="453" height="270" fill="url(#staff-photo)"/>
    </g>
    <path d="M227 0 H453 V118 Q340 150 227 178 Z" fill="url(#gold-fill)"/>
    <path d="M453 0 H680 V92 Q560 98 453 128 Z" fill="#0c0c0c"/>
    <path d="M227 400 Q340 370 453 345 V525 H227 Z" fill="url(#gold-fill)"/>
    <path d="M453 345 Q560 318 680 300 V525 H453 Z" fill="#0c0c0c"/>
    <path d="M453 345 Q560 318 680 300" stroke="#c7a84e" stroke-width="1.5" fill="none"/>
  </svg>

  <div class="panel panel--1">
    <div class="agent">
      <h2 class="heading heading--gold-accent">Your <b>Exclusive Agent</b></h2>
      <div class="rule"></div>
      <p class="body-copy">Lorem ipsum dolor sit amet, consectetur adipiscing elit, sed do eiusmod tempor incididunt ut labore et dolore magna aliqua. Ut enim ad minim veniam, quis nostrud exercitation ullamco laboris nisi ut aliquip ex ea commodo consequat. Duis aute irure dolor in reprehenderit in voluptate velit esse cillum dolore eu fugiat nulla pariatur. Excepteur sint occaecat cupidatat non proident, sunt in culpa qui officia deserunt mollit anim id est laborum.</p>
      <p class="body-copy">Sed ut perspiciatis unde omnis iste natus error sit voluptatem accusantium doloremque laudantium, totam rem aperiam, eaque ipsa quae ab illo inventore veritatis et quasi architecto beatae vitae dicta sunt explicabo.</p>
    </div>
    <div class="photo-frame photo-frame--casino">
      <div class="photo-frame__fill" role="img" aria-label="Casino dealer in a vest serving guests at a gaming table"></div>
    </div>
    <div class="photo-frame photo-frame--warehouse">
      <div class="photo-frame__fill" role="img" aria-label="Warehouse worker in hard hat and safety vest holding a clipboard"></div>
    </div>
  </div>

  <div class="panel panel--2">
    <div class="locations">
      <h2 class="heading">Our <b>Locations</b></h2>
      <div class="rule"></div>
      <ul class="locations__list">
        <li><span>✓</span>NEW YORK</li><li><span>✓</span>DELAWARE</li>
        <li><span>✓</span>PENNSYLVANIA</li><li><span>✓</span>VIRGINIA</li>
        <li><span>✓</span>NEW JERSEY</li><li><span>✓</span>GEORGIA</li>
      </ul>
    </div>
    <div class="contact">
      <div class="contact__pill">CONTACT <b>INFO</b></div>
      <div class="contact__line">
        <svg width="7" height="9" viewBox="0 0 10 14"><path d="M5 0a5 5 0 0 0-5 5c0 4 5 9 5 9s5-5 5-9a5 5 0 0 0-5-5zm0 7a2 2 0 1 1 0-4 2 2 0 0 1 0 4z" fill="#fff"/></svg>
      </div>
      <div class="contact__line">42 Birch Lane, suite 210<br>Oakfield, NJ 08099</div>
      <div class="contact__line">
        <svg width="9" height="9" viewBox="0 0 24 24"><path d="M6.6 10.8a15 15 0 0 0 6.6 6.6l2.2-2.2c.3-.3.7-.4 1-.2 1.1.4 2.3.6 3.6.6.6 0 1 .4 1 1V20c0 .6-.4 1-1 1C10.6 21 3 13.4 3 4c0-.6.4-1 1-1h3.5c.6 0 1 .4 1 1 0 1.3.2 2.5.6 3.6.1.3 0 .7-.2 1z" fill="#fff"/></svg>
        <span class="contact__phone">555-014-2387</span>
      </div>
      <div class="contact__line">✉ info@maplecreststaffing.com</div>
      <div class="contact__line">◍ MapleCrestStaffingServices.com</div>
    </div>
  </div>

  <div class="panel panel--3">
    <div class="brand">
      <span class="brand__dot"></span>
      <span class="brand__name">MAPLE CREST Inc.</span>
    </div>
    <h1 class="tagline">YOUR<br>BEST WAY TO<br><span class="tagline__band">SUCCEED</span></h1>
    <div class="web-pill">MapleCrestStaffingServices.com</div>
  </div>
</section>

<!-- INSIDE SPREAD -->
<section class="spread spread--inside" aria-label="Brochure inside spread">
  <svg class="spread__art" viewBox="0 0 680 525" xmlns="http://www.w3.org/2000/svg">
    <defs>
      <linearGradient id="gold-panel" x1="0" y1="0" x2="0" y2="1">
        <stop offset="0" stop-color="#b39444"/><stop offset="1" stop-color="#8a6d2c"/>
      </linearGradient>
    </defs>
    <rect x="0" y="0" width="227" height="525" fill="#f2f2f2"/>
    <rect x="227" y="0" width="226" height="525" fill="url(#gold-panel)"/>
    <rect x="453" y="0" width="227" height="525" fill="#f0f0f0"/>
    <line x1="14" y1="44" x2="212" y2="44" stroke="#a8893a" stroke-width="1"/>
    <line x1="241" y1="42" x2="439" y2="42" stroke="#ffffff" stroke-width=".8"/>
    <line x1="241" y1="316" x2="439" y2="316" stroke="#ffffff" stroke-width=".8"/>
    <line x1="467" y1="42" x2="666" y2="42" stroke="#a8893a" stroke-width="1"/>
  </svg>

  <div class="panel panel--1">
    <div class="about">
      <h2 class="heading heading--gold-accent" style="color:var(--ink)">About <b style="color:var(--gold)">Us</b></h2>
      <div style="height:10px"></div>
      <span class="tab tab--gold">History</span>
      <p class="body-copy">With more than 18 years of experience Maple Crest Staffing provided staffing services to a wide array of locations, all throughout Pennsylvania. Through the last few years we have expanded to 5 other states including New York, New Jersey, Delaware, Virginia and Georgia. Our ethics are a critical building block of our business and long-term client relationships.</p>
      <span class="tab tab--gold">Culture</span>
      <p class="body-copy">Maple Crest believes in equal opportunity for all, regardless of gender, race, ethnic origin, religion, or handicap. Our employees are our most valuable asset. We strive to create a work environment of professionalism, trust and respect; CLIENT SATISFACTION.</p>
      <span class="tab tab--gold">Mission</span>
      <p class="body-copy">Maple Crest is more than a staffing company; we want to become your business partner. Through our partnership-network programs we can help you reduce the hard-costs of your business expenses, including payroll taxes and benefits.</p>
      <span class="tab tab--gold">Our Process</span>
      <p class="body-copy">Our screening process includes a thorough interview with each potential candidate to give us insight into previous work history, skills, communication abilities and career goals.</p>
      <span class="tab tab--gold">Staffing Solutions</span>
      <p class="body-copy">Maple Crest's personalized services, expertise and affordable rates are key factors of our success and being our client's choice staffing agency.</p>
    </div>
    <div class="team-photo" role="img" aria-label="Group of workers from many trades: chef, builder, nurse, mechanic and office staff"></div>
  </div>

  <div class="panel panel--2">
    <div class="why-staffing">
      <h2 class="heading">Why <b>Staffing?</b></h2>
      <div style="height:8px"></div>
      <span class="tab tab--black">Avoid Unemployment Claims</span>
      <p class="body-copy">The temporary staff personnel is an employee of the staffing agency, so there is no concern about unemployment when their services are no longer needed.</p>
      <span class="tab tab--black">Improve Productivity</span>
      <p class="body-copy">By bringing in temporary staff to handle the extra work-load, your full-time employees can continue to focus on their main job tasks.</p>
      <span class="tab tab--black">Increasing Flexibility</span>
      <p class="body-copy">Temporary employees can be brought in to cover the vacation of an employee or a seasonal work, whether it is a few hours a week or full-time.</p>
      <span class="tab tab--black">Decrease Cost</span>
      <p class="body-copy">Employing temporary staff can decrease overhead costs such as overtime for regular, full-time employees as well as additional benefits.</p>
      <span class="tab tab--black">Contract To Hire</span>
      <p class="body-copy">Reduce the risk of making a bad hire by evaluating a candidate's performance in your work environment first.</p>
    </div>
    <div class="industries">
      <h2 class="heading">Industries <b>We Serve</b></h2>
      <ul class="industries__list">
        <li>WAREHOUSING</li><li>HOTEL</li><li>CASINO</li><li>PAPER MAILLING</li>
        <li>TRANSPORTATION</li><li>LANDFILL</li><li>FOOD HANDLING</li>
      </ul>
    </div>
  </div>
  <div class="consultant-photo" role="img" aria-label="Smiling staffing consultant in shirt and tie holding a clipboard"></div>

  <div class="panel panel--3">
    <div class="why-choose">
      <h2 class="heading heading--gold-accent" style="color:var(--ink)">Why Choose <b style="color:var(--gold)">Our Services?</b></h2>
      <div style="height:8px"></div>
      <p class="body-copy">Our commitment is to deliver the highest possible level of service, professionalism and integrity. Our focus is on delivering results and building long term client relationships by providing top quality candidates.</p>
      <p class="body-copy"><span class="subhead">Employee Benefits:</span> Workers are paid on a timely weekly basis. Our system responds to workers' need for payment immediately.</p>
      <p class="body-copy"><span class="subhead">Workers' Compensation:</span> We provide workers' compensation for our employees while on assignment and handle all claims and expenses.</p>
      <span class="tab tab--black">Availability and Flexibility</span>
      <p class="body-copy">Our temporary staff has proven to be available and ready for work in a timely and efficient manner, crafted to your needs and specifications.</p>
      <span class="tab tab--black">We Save you both TIME and MONEY</span>
      <p class="body-copy">Competitive rates to keep your business on budget. We bill only for employee hours approved by you. Our business was built on a strong reputation for quality service and a deep understanding of the job market.</p>
      <p class="body-copy closing">When you are looking for a qualified candidate or when you need a new job, trust the experts at Maple Crest Staffing Services. Let us put our world-class customer service and staffing expertise to work for you!</p>
    </div>
    <div class="slogan">
      <div class="slogan__main">CONNECTING<br>OPPORTUNITY</div>
      <div class="slogan__strip">WITH TODAY'S TOP TALENT</div>
    </div>
  </div>
</section>

</body>
</html>
```